Business Cards used to invite people to our church

We are a church and have need of a business card sized advertisement that allows our members to hand them out in order to invite people to the church. I need the front of the card to say "You're Invited" or "Come Check us out". with the service times on the back of the card later.
I have attached one of the OLD cards we have used in the past, but we want a complete makeover, into a more modern style that does not require the image.
I am also replacing the old logo with a newer "flat" logo which is attached.
Please use marketing colors. (blue or red or something that catches attention)
Create a card that DOES NOT have the picture of the two people on the front
The information on the sample card back is correct to go onto new card
Target Market(s)
anyone
Industry/Entity Type
Business
Contact Information for Business Card
sertice times and address information which you can get from the sample card I uploaded. It should have "You're Invited" or "Come Check us out" on the front of the card with out logo.

```html
<!DOCTYPE html>
<html lang="en">
<head>
<meta charset="utf-8">
<title>Grace Harbor Invitation Card</title>
<link href="https://fonts.googleapis.com/css2?family=EB+Garamond&family=Open+Sans:wght@400;800&family=Federo&family=Yellowtail&display=swap" rel="stylesheet">
<style>
  :root {
    --ink: #111111;
    --brand-blue: #0d4ea6;
    --trim-grey: #4f6468;
    --trim-blue: #2f7fd6;
    --sky-light: #d9f1fb;
    --sky-mid: #9fdcf4;
    --sky-deep: #5cc4ec;
    --paper: #ffffff;
  }
  html, body {
    margin: 0;
    padding: 0;
    width: 1200px;
    height: 1200px;
    overflow: hidden;
    background: var(--paper);
  }
  .canvas {
    position: relative;
    width: 1200px;
    height: 1200px;
  }
  .crop-marks {
    position: absolute;
    inset: 0;
  }
  .card {
    position: absolute;
    left: 95px;
    width: 971px;
    height: 484px;
    overflow: hidden;
    background: var(--paper);
  }
  .card--back { top: 74px; }
  .card--front { top: 674px; }
  .sky {
    position: absolute;
    left: 0;
    right: 0;
    bottom: 0;
  }
  .card--back .sky {
    top: 196px;
    background:
      radial-gradient(ellipse 40% 50% at 20% 80%, rgba(255,255,255,.85), transparent 70%),
      radial-gradient(ellipse 35% 45% at 85% 90%, rgba(255,255,255,.8), transparent 70%),
      linear-gradient(180deg, var(--paper) 0%, var(--sky-light) 20%, var(--sky-mid) 55%, var(--sky-deep) 100%);
  }
  .card--front .sky {
    top: 110px;
    background:
      radial-gradient(ellipse 45% 40% at 30% 95%, rgba(255,255,255,.85), transparent 70%),
      radial-gradient(ellipse 30% 40% at 90% 85%, rgba(255,255,255,.7), transparent 70%),
      linear-gradient(180deg, var(--paper) 0%, var(--paper) 25%, var(--sky-light) 55%, var(--sky-mid) 85%, var(--sky-deep) 100%);
  }
  .site, .address, .phone {
    position: absolute;
    left: 0;
    right: 0;
    margin: 0;
    text-align: center;
    font-family: "EB Garamond", Georgia, serif;
    color: var(--ink);
    font-weight: 400;
    white-space: nowrap;
  }
  .site { top: 18px; font-size: 60px; letter-spacing: 1px; }
  .address { top: 99px; font-size: 39px; }
  .phone { top: 166px; font-size: 55px; letter-spacing: 1px; }
  .schedule {
    position: absolute;
    left: 109px;
    width: 760px;
    top: 268px;
    margin: 0;
    padding: 0;
    list-style: none;
    font-family: "Open Sans", Arial, sans-serif;
    color: var(--ink);
  }
  .schedule li {
    display: flex;
    align-items: baseline;
    height: 60px;
    font-size: 31px;
  }
  .schedule .day { font-weight: 800; letter-spacing: -0.5px; }
  .schedule .leader {
    flex: 1;
    border-bottom: 3px dotted var(--ink);
    margin: 0 2px;
    transform: translateY(-6px);
  }
  .schedule .time { font-weight: 400; }
  .brand-name {
    position: absolute;
    left: 58px;
    top: 88px;
    margin: 0;
    font-family: "Federo", "Trebuchet MS", sans-serif;
    font-size: 66px;
    line-height: 1.05;
    color: var(--brand-blue);
    font-weight: 400;
  }
  .pastors {
    position: absolute;
    left: 427px;
    top: 82px;
    margin: 0;
    font-family: "Federo", "Trebuchet MS", sans-serif;
    font-size: 54px;
    line-height: 92px;
    color: var(--ink);
    font-variant: small-caps;
    font-weight: 400;
  }
  .invite {
    position: absolute;
    left: 0;
    right: 0;
    top: 250px;
    margin: 0;
    text-align: center;
    font-family: "Yellowtail", cursive;
    font-size: 112px;
    color: var(--brand-blue);
    font-weight: 400;
    transform: translateX(-12px);
  }
</style>
</head>
<body>
<main class="canvas">
  <svg class="crop-marks" width="1200" height="1200" viewBox="0 0 1200 1200" aria-hidden="true">
    <g fill="none" stroke="var(--trim-grey)" stroke-width="3">
      <path d="M94 24 V72 H56"/>
      <path d="M1066 24 V72 H1106"/>
      <path d="M94 612 V674 H56"/>
      <path d="M1066 612 V674 H1100"/>
    </g>
    <line x1="94" y1="73" x2="1066" y2="73" stroke="var(--trim-grey)" stroke-width="1"/>
    <line x1="94" y1="674" x2="1066" y2="674" stroke="var(--trim-blue)" stroke-width="1.5"/>
  </svg>

  <section class="card card--back">
    <div class="sky" role="img" aria-label="Soft blue sky with white clouds"></div>
    <h1 class="site">GRACEHARBOR.ORG</h1>
    <p class="address">2740 W. CEDAR LANE - MAPLE GROVE, TX 75099</p>
    <p class="phone">1-800-555-0142</p>
    <ul class="schedule">
      <li><span class="day">SUNDAY</span><span class="leader"></span><span class="time">9:00 AM</span></li>
      <li><span class="day">&nbsp;SUNDAY&nbsp;</span><span class="leader"></span><span class="time">11:00 AM</span></li>
      <li><span class="day">WED. BIBLE CLASS.</span><span class="leader"></span><span class="time">7:00 PM</span></li>
    </ul>
  </section>

  <section class="card card--front">
    <div class="sky" role="img" aria-label="Soft blue sky with white clouds"></div>
    <p class="brand-name">Grace<br>Harbor</p>
    <p class="pastors">Pastor Daniel<br>&amp;Ruth Mercer</p>
    <h2 class="invite">You're Invited</h2>
  </section>
</main>
</body>
</html>
```